We need our website look and feel updated to match our brand

We are looking to update our website and a "where to buy" tab at the top of the website. The current look and feel is ok but needs a clean up. The task is as follows:
1. Update the current pages and add a page for "Where to Buy"
2. Update the product page to reflect our current products. ie we have only three products now. Undercoat K, Undercoat M and GLAZEX. This page will have very similar descriptions and at the bottom of each product will be a link to our SDS (safety data sheets).
3. Please visit our current website for the look and feel.
4. Use our New Taglines need to be included. "Always Cleaning. All the Time." "24/7 SAFE SURFACE PROTECTION" (Logo as well)
5. The HomePage will need a nice clean location to our corporate video. https://clipvue.net/8kRtWmPzQaL (link for viewing) that will be the highlight and easy to access on the homepage.
Some examples of websites we like.
https://velmarix.com/
https://quorbelhall.com/ (like the use of motion graphics in these)
Our focus claims are that our product is a surface cleaner and deodorizer. We would like to see variations in black, white background (Black header bar) and Gray backgrounds.

```html
<!DOCTYPE html>
<html lang="en">
<head>
<meta charset="utf-8">
<title>Novacoat – Homepage Variations</title>
<link href="https://fonts.googleapis.com/css2?family=Roboto+Condensed:wght@700&family=Lato:wght@400;700&display=swap" rel="stylesheet">
<style>
:root{
  --board:#eff0f2;
  --yellow:#f7c31a;
  --black:#050505;
  --white:#ffffff;
  --ink:#1a1a1a;
  --head:"Roboto Condensed", Arial Narrow, sans-serif;
  --body:"Lato", Arial, sans-serif;
}
*{box-sizing:border-box;margin:0;padding:0}
html,body{width:898px;height:1200px;overflow:hidden;background:var(--board)}
.board{position:relative;width:898px;height:1200px;background:var(--board)}
.page{position:absolute;top:47px;width:630px;height:2039px;transform:scale(.5426);transform-origin:0 0;font-family:var(--body);color:var(--white);overflow:hidden;background:var(--black)}
.page--dark{left:80px}
.page--light{left:476px}
.section{position:absolute;left:0;width:630px}
.abs{position:absolute}
.h2{font-family:var(--head);font-weight:700;font-size:21px;letter-spacing:.2px;text-transform:uppercase}
.center{left:0;width:630px;text-align:center}
.copy{font-size:7.3px;line-height:13.5px;color:#d8d8d8}
.copy p+p{margin-top:6px}
.btn{position:absolute;display:flex;align-items:center;justify-content:center;gap:5px;height:24px;padding:0 9px;background:var(--yellow);color:var(--ink);font-family:var(--body);font-size:8px;font-weight:700;text-transform:uppercase;text-decoration:none;border-radius:1px}
.btn svg{width:7px;height:7px}

/* header */
.hero{top:0;height:359px;background:#000}
.logo{position:absolute;display:flex;align-items:center;gap:3px;font-family:var(--body);font-weight:700;color:var(--white);white-space:nowrap}
.logo__mark{background:var(--yellow)}
.nav{left:58px;top:11px}
.nav .logo__mark{width:8px;height:8px}
.nav .logo{font-size:11px}
.menu{position:absolute;left:128px;top:16px;display:flex;gap:12px;font-size:7.6px;text-transform:uppercase;color:var(--white);white-space:nowrap}
.menu span:first-child{color:var(--yellow)}
.hero__photo{position:absolute;left:300px;top:0;width:330px;height:359px;background:radial-gradient(ellipse 90px 140px at 68% 30%,#e9e9e6 0%,#a8a8a3 45%,transparent 70%),radial-gradient(ellipse 260px 120px at 20% 70%,rgba(170,170,170,.45),transparent 70%),radial-gradient(ellipse 80px 90px at 80% 80%,#b98b6e,transparent 70%),#000}
.hero__mist{position:absolute;left:0;top:220px;width:330px;height:139px;background:radial-gradient(ellipse 330px 90px at 50% 80%,rgba(120,120,120,.4),transparent 70%)}
.kicker{left:60px;top:124px;font-family:var(--head);font-weight:700;font-size:22px;color:var(--yellow)}
.hero__title{left:60px;top:158px;font-family:var(--head);font-weight:700;font-size:26px;line-height:28px}

/* about */
.about{top:359px;height:293px;background:var(--black)}
.frame{position:absolute;display:block;border:2px solid var(--yellow);padding:4px}
.frame__fill{width:100%;height:100%}
.about .frame{left:62px;top:38px;width:219px;height:209px}
.about__photo{background:linear-gradient(120deg,#6f4d3e 0%,#c48f76 40%,#3b3d47 65%,#d6d6d8 100%)}
.about__title{left:309px;top:34px}
.about__copy{left:309px;top:64px;width:262px}

/* products */
.products{top:652px;height:283px;background:linear-gradient(180deg,#0b0b0b,#111 60%,#0b0b0b)}
.products .h2{top:28px}
.card{position:absolute;top:71px;width:117px;height:182px;background:#060606;border:1px solid #1f1f1f;text-align:center}
.card__img{margin:4px;height:92px;background:radial-gradient(ellipse 20px 38px at 50% 55%,#f0a93a,#b88426 70%,transparent 72%),#1a1a1a}
.card__img--silver{background:radial-gradient(ellipse 20px 38px at 50% 55%,#f1f1f1,#a9a9a9 70%,transparent 72%),#1a1a1a}
.card__img--pale{background:radial-gradient(ellipse 20px 38px at 50% 55%,#f6e3a0,#c9a23d 70%,transparent 72%),#1a1a1a}
.card__name{margin-top:15px;font-size:7px;font-weight:700;text-transform:uppercase}
.card__stars{margin-top:3px;font-size:8px;letter-spacing:1px;color:var(--yellow);line-height:10px}
.card__price{margin-top:3px;font-family:var(--head);font-size:9px}
.card .btn{left:25px;top:152px;height:20px;width:66px;font-size:6.5px;padding:0}
.card .btn svg{width:10px;height:8px}

/* technology */
.tech{top:935px;height:301px;background:var(--black)}
.tech__title{left:58px;top:50px}
.tech__copy{left:58px;top:76px;width:278px}
.tech .frame{left:366px;top:45px;width:206px;height:210px}
.tech__art{position:relative;background:linear-gradient(180deg,#d9dce3 0%,#c7ccd6 45%,#e8c96a 60%,#f2d98a 100%)}
.play{position:absolute;left:50%;top:50%;width:26px;height:26px;margin:-13px 0 0 -13px}

/* banner */
.banner{top:1236px;height:158px;background:linear-gradient(180deg,#131313,#0e0e0e)}
.banner__title{top:42px;font-family:var(--head);font-weight:700;font-size:19px;line-height:20px;text-transform:uppercase}
.banner .btn{left:275px;top:92px;width:80px}

/* projects */
.projects{top:1394px;height:359px;background:var(--black)}
.projects .h2{top:43px}
.tile{position:absolute}
.tile--lab{background:linear-gradient(135deg,#1a2c55,#5b79a8 50%,#1c2f5c)}
.tile--chem{background:linear-gradient(160deg,#2f7fc9,#5fb4e6 50%,#1b4f8f)}
.tile--glass{background:linear-gradient(180deg,#7c6fb6,#b39ad0 40%,#e4b46f 60%,#4d4f8a)}
.tile--tubes{background:linear-gradient(150deg,#0f2d66,#3f7fc4 50%,#0c2552)}
.tile--room{background:linear-gradient(180deg,#9fd2f0,#3f8fd0 60%,#1f5a98)}

/* footer */
.footer{top:1753px;height:286px;background:#070707}
.footer .logo{left:60px;top:40px;font-size:28px;font-weight:400;gap:5px}
.footer .logo__mark{width:16px;height:16px}
.footer__blurb{left:60px;top:96px;width:145px;font-size:7.3px;line-height:13.5px;color:#dcdcdc}
.fhead{position:absolute;font-size:7px;font-weight:700;text-transform:uppercase;text-decoration:underline;color:var(--white)}
.socials{position:absolute;left:60px;top:161px;display:flex;gap:6px}
.socials span{width:18px;height:18px;border:1px solid var(--white);border-radius:50%}
.contact-row{position:absolute;left:244px;display:flex;align-items:center;gap:8px;font-size:7.3px;white-space:nowrap}
.contact-row svg{width:17px;height:17px}
.links{position:absolute;top:63px;font-size:7.3px;line-height:20px}
.links li{list-style:none;white-space:nowrap}
.links li::before{content:"»";margin-right:8px}
.news{position:absolute;left:59px;top:218px;width:167px;height:23px;display:flex;background:#111;border:1px solid #1d1d1d}
.news__field{flex:1;display:flex;align-items:center;gap:6px;padding-left:8px;font-size:6.5px;color:#888}
.news__field svg{width:8px;height:7px}
.news__btn{width:61px;display:flex;align-items:center;justify-content:center;background:var(--yellow);color:var(--ink);font-size:7px;font-weight:700;text-transform:uppercase}
.badge{position:absolute;top:207px;height:34px;border:1.5px solid var(--yellow);border-radius:3px}
.copyright{top:266px;font-size:6.8px;color:#d0d0d0}

/* light variant */
.page--light .about,.page--light .tech{background:var(--white);color:var(--ink)}
.page--light .about .copy,.page--light .tech .copy{color:#333}
.page--light .products{background:linear-gradient(180deg,#e7ecef,#f4f6f7 50%,#e6ebee);color:var(--ink)}
.page--light .card{background:var(--white);border-color:#d8d8d8}
.page--light .card__img{background-color:#eeeeee}
.page--light .banner{background:linear-gradient(180deg,#f3c62a,#f0c013);color:var(--ink)}
.page--light .banner .btn{background:var(--black);color:var(--yellow)}
.page--light .projects{background:linear-gradient(180deg,#ffffff,#f4f7f9);color:var(--ink)}
.page--light .news{background:var(--white)}
</style>
</head>
<body>
<div class="board">

<!-- ===== Dark variation ===== -->
<div class="page page--dark">
  <section class="section hero">
    <div class="hero__photo" role="img" aria-label="Hand holding a spray gun releasing a fine mist"><div class="hero__mist"></div></div>
    <div class="nav abs"><div class="logo"><span class="logo__mark"></span>Novacoat</div></div>
    <nav class="menu"><span>Home</span><span>About Us</span><span>Where to buy</span><span>Products</span><span>Our Technology</span><span>News</span><span>FAQ</span><span>Contact</span><span>&#9906;</span></nav>
    <div class="abs kicker">ALWAYS CLEANING</div>
    <h1 class="abs hero__title">ALL THE TIME 24/7 SAFE<br>SURFACE PROTECTION</h1>
    <a class="btn" style="left:60px;top:227px" href="#">Get Started <svg viewBox="0 0 10 10"><circle cx="5" cy="5" r="5" fill="currentColor"/><path d="M4 2.8 6.2 5 4 7.2" stroke="#f7c31a" stroke-width="1.4" fill="none"/></svg></a>
  </section>

  <section class="section about">
    <div class="frame"><div class="frame__fill about__photo" role="img" aria-label="Business handshake between two people in suits"></div></div>
    <h2 class="abs h2 about__title">About Novacoat</h2>
    <div class="abs copy about__copy">
      <p>The onset of COVID-19 has changed our lives forever.The current methods of cleaning surfaces are not sustainable. Cleaning the environ ment we live in with caustic UV-C light, ammonia-based cleaners and other harsh chemicals is wasteful. The moment you clean the surface an infected person touches that surface again it requires reapplication of your protective cleaners.</p>
      <p>Novacoat is bringing a permanent surface coating formula to the United States market. A titanium dioxide photocatalyst coating that is incredibly long lasting and durable. How long basically lasts a long as the substrate is present. As long as not mechanically removed or painted over Novacoat lasts for decades on any surface, indoor or outdoor.</p>
    </div>
    <a class="btn" style="left:309px;top:224px" href="#">Get Started <svg viewBox="0 0 10 10"><circle cx="5" cy="5" r="5" fill="currentColor"/><path d="M4 2.8 6.2 5 4 7.2" stroke="#f7c31a" stroke-width="1.4" fill="none"/></svg></a>
  </section>

  <section class="section products">
    <h2 class="abs h2 center">Novacoat Products</h2>
    <div class="card" style="left:63px"><div class="card__img" role="img" aria-label="Orange gallon jug of Undercoat K"></div><div class="card__name">Novacoat UV-A</div><div class="card__stars">★★★★★</div><div class="card__price">$ 49.2</div><a class="btn" href="#"><svg viewBox="0 0 12 10"><path d="M0 1h2l1.5 5.5h6L11 3H3" stroke="currentColor" fill="none"/><circle cx="4.5" cy="8.5" r="1" fill="currentColor"/><circle cx="9" cy="8.5" r="1" fill="currentColor"/></svg>Buy Now</a></div>
    <div class="card" style="left:192px"><div class="card__img card__img--silver" role="img" aria-label="Silver gallon jug of Undercoat M"></div><div class="card__name">Novacoat Binder</div><div class="card__stars">★★★★★</div><div class="card__price">$ 49.2</div><a class="btn" href="#"><svg viewBox="0 0 12 10"><path d="M0 1h2l1.5 5.5h6L11 3H3" stroke="currentColor" fill="none"/><circle cx="4.5" cy="8.5" r="1" fill="currentColor"/><circle cx="9" cy="8.5" r="1" fill="currentColor"/></svg>Buy Now</a></div>
    <div class="card" style="left:321px"><div class="card__img card__img--pale" role="img" aria-label="Pale yellow gallon jug of GLAZEX"></div><div class="card__name">Novacoat Visible Light</div><div class="card__stars">★★★★★</div><div class="card__price">$ 49.2</div><a class="btn" href="#"><svg viewBox="0 0 12 10"><path d="M0 1h2l1.5 5.5h6L11 3H3" stroke="currentColor" fill="none"/><circle cx="4.5" cy="8.5" r="1" fill="currentColor"/><circle cx="9" cy="8.5" r="1" fill="currentColor"/></svg>Buy Now</a></div>
    <div class="card" style="left:449px"><div class="card__img" role="img" aria-label="Orange gallon jug of Undercoat K"></div><div class="card__name">Novacoat UV-B</div><div class="card__stars">★★★★★</div><div class="card__price">$ 49.2</div><a class="btn" href="#"><svg viewBox="0 0 12 10"><path d="M0 1h2l1.5 5.5h6L11 3H3" stroke="currentColor" fill="none"/><circle cx="4.5" cy="8.5" r="1" fill="currentColor"/><circle cx="9" cy="8.5" r="1" fill="currentColor"/></svg>Buy Now</a></div>
  </section>

  <section class="section tech">
    <h2 class="abs h2 tech__title">Novacoat Technology</h2>
    <div class="abs copy tech__copy">
      <p>The onset of COVID-19 has changed our lives forever. The current methods of cleaning surfaces are not sustainable. Cleaning the environment, we live in with caustic UV-C light, ammonia-based cleaners and other harsh chemicals is wasteful.The moment you clean the surface and an infected person touches that surface again it requires reapplication of whatever you are using to keep the surfaces clean and safe.</p>
      <p>Novacoat is bringing a permanent surface coating formula to the United States market. A titanium dioxide photocatalyst coating that is incredibly long lasting and durable.How long? It basically lasts a long as the substrate is present. As long as it's not mechanically removed, Novacoat lasts for decades on any surface, indoor or outdoor.</p>
    </div>
    <a class="btn" style="left:58px;top:231px" href="#">Get Started <svg viewBox="0 0 10 10"><circle cx="5" cy="5" r="5" fill="currentColor"/><path d="M4 2.8 6.2 5 4 7.2" stroke="#f7c31a" stroke-width="1.4" fill="none"/></svg></a>
    <div class="frame"><div class="frame__fill tech__art" role="img" aria-label="Corporate video still: illustrated workers in protective suits spraying a classroom"><svg class="play" viewBox="0 0 26 26"><circle cx="13" cy="13" r="12" fill="#fff" stroke="#f7c31a" stroke-width="2"/><path d="M10.5 8.5v9l7-4.5z" fill="#111"/></svg></div></div>
  </section>

  <section class="section banner">
    <h2 class="abs center banner__title">Novacoat is the world's first permanent<br>surface cleaner</h2>
    <a class="btn" href="#">Join Now <svg viewBox="0 0 10 10"><circle cx="5" cy="5" r="5" fill="currentColor"/><path d="M4 2.8 6.2 5 4 7.2" stroke="#f7c31a" stroke-width="1.4" fill="none"/></svg></a>
  </section>

  <section class="section projects">
    <h2 class="abs h2 center">Novacoat Projects</h2>
    <div class="tile tile--lab" style="left:59px;top:85px;width:182px;height:83px" role="img" aria-label="Scientists working in a laboratory"></div>
    <div class="tile tile--chem" style="left:59px;top:175px;width:182px;height:139px" role="img" aria-label="Hand pouring red liquid into a beaker"></div>
    <div class="tile tile--glass" style="left:249px;top:85px;width:182px;height:229px" role="img" aria-label="Laboratory glassware with science icons"></div>
    <div class="tile tile--tubes" style="left:438px;top:85px;width:134px;height:111px" role="img" aria-label="Test tubes beside a microscope"></div>
    <div class="tile tile--room" style="left:438px;top:203px;width:134px;height:111px" role="img" aria-label="Clean hospital operating room"></div>
  </section>

  <footer class="section footer">
    <div class="logo"><span class="logo__mark"></span>Novacoat</div>
    <p class="abs footer__blurb">Our US company was formed to take advantage of 20 years of experience with Titanium Dioxide in Japan.</p>
    <div class="fhead" style="left:60px;top:143px">Connect with us</div>
    <div class="socials"><span></span><span></span><span></span><span></span></div>
    <div class="fhead" style="left:244px;top:45px">Contact us</div>
    <div class="contact-row" style="top:65px"><svg viewBox="0 0 17 17"><circle cx="8.5" cy="8.5" r="8" fill="none" stroke="#fff"/><path d="M6 5.5l1.3-.3.8 1.8-.9.7a5 5 0 0 0 2.2 2.2l.7-.9 1.8.8-.3 1.3c-3 .3-5.8-2.6-5.6-5.6z" fill="#fff"/></svg>+ 555 (0142) 730</div>
    <div class="contact-row" style="top:97px"><svg viewBox="0 0 17 17"><circle cx="8.5" cy="8.5" r="8" fill="none" stroke="#fff"/><rect x="5" y="6" width="7" height="5" fill="none" stroke="#fff"/><path d="M5 6l3.5 3L12 6" fill="none" stroke="#fff"/></svg>contactus@novacoat.com</div>
    <div class="contact-row" style="top:129px"><svg viewBox="0 0 17 17"><circle cx="8.5" cy="8.5" r="8" fill="none" stroke="#fff"/><path d="M8.5 12.5s-3-3-3-5a3 3 0 0 1 6 0c0 2-3 5-3 5z" fill="none" stroke="#fff"/><circle cx="8.5" cy="7.5" r="1" fill="#fff"/></svg>Location: Elmridge, CT USA</div>
    <div class="fhead" style="left:417px;top:45px">Otherlinks</div>
    <ul class="links" style="left:417px"><li>Team</li><li>FAQ</li><li>Services</li><li>Privacy</li><li>Policy</li></ul>
    <div class="fhead" style="left:512px;top:45px">Quicklinks</div>
    <ul class="links" style="left:512px"><li>Home</li><li>About Us</li><li>where to buy</li><li>Products</li><li>More</li><li>Contact</li></ul>
    <div class="fhead" style="left:59px;top:205px">Sign up for newsletter</div>
    <div class="news"><div class="news__field"><svg viewBox="0 0 8 7"><rect x=".5" y=".5" width="7" height="6" fill="none" stroke="#f7c31a"/><path d="M.5 .5 4 4l3.5-3.5" fill="none" stroke="#f7c31a"/></svg>Enter Your Email:</div><div class="news__btn">Subscribe</div></div>
    <div class="badge" style="left:260px;width:60px"></div>
    <div class="badge" style="left:352px;width:128px"></div>
    <div class="badge" style="left:512px;width:60px"></div>
    <p class="abs center copyright">Copyright © 2022 Novacoat All right Reserved.</p>
  </footer>
</div>

<!-- ===== Light variation ===== -->
<div class="page page--light">
  <section class="section hero">
    <div class="hero__photo" role="img" aria-label="Hand holding a spray gun releasing a fine mist"><div class="hero__mist"></div></div>
    <div class="nav abs"><div class="logo"><span class="logo__mark"></span>Novacoat</div></div>
    <nav class="menu"><span>Home</span><span>About Us</span><span>Where to buy</span><span>Products</span><span>Our Technology</span><span>News</span><span>FAQ</span><span>Contact</span><span>&#9906;</span></nav>
    <div class="abs kicker">ALWAYS CLEANING</div>
    <h1 class="abs hero__title">ALL THE TIME 24/7 SAFE<br>SURFACE PROTECTION</h1>
    <a class="btn" style="left:60px;top:227px" href="#">Get Started <svg viewBox="0 0 10 10"><circle cx="5" cy="5" r="5" fill="currentColor"/><path d="M4 2.8 6.2 5 4 7.2" stroke="#f7c31a" stroke-width="1.4" fill="none"/></svg></a>
  </section>

  <section class="section about">
    <div class="frame"><div class="frame__fill about__photo" role="img" aria-label="Business handshake between two people in suits"></div></div>
    <h2 class="abs h2 about__title">About Novacoat</h2>
    <div class="abs copy about__copy">
      <p>The onset of COVID-19 has changed our lives forever.The current methods of cleaning surfaces are not sustainable. Cleaning the environ ment we live in with caustic UV-C light, ammonia-based cleaners and other harsh chemicals is wasteful. The moment you clean the surface an infected person touches that surface again it requires reapplication of your protective cleaners.</p>
      <p>Novacoat is bringing a permanent surface coating formula to the United States market. A titanium dioxide photocatalyst coating that is incredibly long lasting and durable. How long basically lasts a long as the substrate is present. As long as not mechanically removed or painted over Novacoat lasts for decades on any surface, indoor or outdoor.</p>
    </div>
    <a class="btn" style="left:309px;top:224px" href="#">Get Started <svg viewBox="0 0 10 10"><circle cx="5" cy="5" r="5" fill="currentColor"/><path d="M4 2.8 6.2 5 4 7.2" stroke="#f7c31a" stroke-width="1.4" fill="none"/></svg></a>
  </section>

  <section class="section products">
    <h2 class="abs h2 center">Novacoat Products</h2>
    <div class="card" style="left:63px"><div class="card__img" role="img" aria-label="Orange gallon jug of Undercoat K"></div><div class="card__name">Novacoat UV-A</div><div class="card__stars">★★★★★</div><div class="card__price">$ 49.2</div><a class="btn" href="#"><svg viewBox="0 0 12 10"><path d="M0 1h2l1.5 5.5h6L11 3H3" stroke="currentColor" fill="none"/><circle cx="4.5" cy="8.5" r="1" fill="currentColor"/><circle cx="9" cy="8.5" r="1" fill="currentColor"/></svg>Buy Now</a></div>
    <div class="card" style="left:192px"><div class="card__img card__img--silver" role="img" aria-label="Silver gallon jug of Undercoat M"></div><div class="card__name">Novacoat Binder</div><div class="card__stars">★★★★★</div><div class="card__price">$ 49.2</div><a class="btn" href="#"><svg viewBox="0 0 12 10"><path d="M0 1h2l1.5 5.5h6L11 3H3" stroke="currentColor" fill="none"/><circle cx="4.5" cy="8.5" r="1" fill="currentColor"/><circle cx="9" cy="8.5" r="1" fill="currentColor"/></svg>Buy Now</a></div>
    <div class="card" style="left:321px"><div class="card__img card__img--pale" role="img" aria-label="Pale yellow gallon jug of GLAZEX"></div><div class="card__name">Novacoat Visible Light</div><div class="card__stars">★★★★★</div><div class="card__price">$ 49.2</div><a class="btn" href="#"><svg viewBox="0 0 12 10"><path d="M0 1h2l1.5 5.5h6L11 3H3" stroke="currentColor" fill="none"/><circle cx="4.5" cy="8.5" r="1" fill="currentColor"/><circle cx="9" cy="8.5" r="1" fill="currentColor"/></svg>Buy Now</a></div>
    <div class="card" style="left:449px"><div class="card__img" role="img" aria-label="Orange gallon jug of Undercoat K"></div><div class="card__name">Novacoat UV-B</div><div class="card__stars">★★★★★</div><div class="card__price">$ 49.2</div><a class="btn" href="#"><svg viewBox="0 0 12 10"><path d="M0 1h2l1.5 5.5h6L11 3H3" stroke="currentColor" fill="none"/><circle cx="4.5" cy="8.5" r="1" fill="currentColor"/><circle cx="9" cy="8.5" r="1" fill="currentColor"/></svg>Buy Now</a></div>
  </section>

  <section class="section tech">
    <h2 class="abs h2 tech__title">Novacoat Technology</h2>
    <div class="abs copy tech__copy">
      <p>The onset of COVID-19 has changed our lives forever. The current methods of cleaning surfaces are not sustainable. Cleaning the environment, we live in with caustic UV-C light, ammonia-based cleaners and other harsh chemicals is wasteful.The moment you clean the surface and an infected person touches that surface again it requires reapplication of whatever you are using to keep the surfaces clean and safe.</p>
      <p>Novacoat is bringing a permanent surface coating formula to the United States market. A titanium dioxide photocatalyst coating that is incredibly long lasting and durable.How long? It basically lasts a long as the substrate is present. As long as it's not mechanically removed, Novacoat lasts for decades on any surface, indoor or outdoor.</p>
    </div>
    <a class="btn" style="left:58px;top:231px" href="#">Get Started <svg viewBox="0 0 10 10"><circle cx="5" cy="5" r="5" fill="currentColor"/><path d="M4 2.8 6.2 5 4 7.2" stroke="#f7c31a" stroke-width="1.4" fill="none"/></svg></a>
    <div class="frame"><div class="frame__fill tech__art" role="img" aria-label="Corporate video still: illustrated workers in protective suits spraying a classroom"><svg class="play" viewBox="0 0 26 26"><circle cx="13" cy="13" r="12" fill="#fff" stroke="#f7c31a" stroke-width="2"/><path d="M10.5 8.5v9l7-4.5z" fill="#111"/></svg></div></div>
  </section>

  <section class="section banner">
    <h2 class="abs center banner__title">Novacoat is the world's first permanent<br>surface cleaner</h2>
    <a class="btn" href="#">Join Now <svg viewBox="0 0 10 10"><circle cx="5" cy="5" r="5" fill="#f7c31a"/><path d="M4 2.8 6.2 5 4 7.2" stroke="#050505" stroke-width="1.4" fill="none"/></svg></a>
  </section>

  <section class="section projects">
    <h2 class="abs h2 center">Novacoat Projects</h2>
    <div class="tile tile--lab" style="left:59px;top:85px;width:182px;height:83px" role="img" aria-label="Scientists working in a laboratory"></div>
    <div class="tile tile--chem" style="left:59px;top:175px;width:182px;height:139px" role="img" aria-label="Hand pouring red liquid into a beaker"></div>
    <div class="tile tile--glass" style="left:249px;top:85px;width:182px;height:229px" role="img" aria-label="Laboratory glassware with science icons"></div>
    <div class="tile tile--tubes" style="left:438px;top:85px;width:134px;height:111px" role="img" aria-label="Test tubes beside a microscope"></div>
    <div class="tile tile--room" style="left:438px;top:203px;width:134px;height:111px" role="img" aria-label="Clean hospital operating room"></div>
  </section>

  <footer class="section footer">
    <div class="logo"><span class="logo__mark"></span>Novacoat</div>
    <p class="abs footer__blurb">Our US company was formed to take advantage of 20 years of experience with Titanium Dioxide in Japan.</p>
    <div class="fhead" style="left:60px;top:143px">Connect with us</div>
    <div class="socials"><span></span><span></span><span></span><span></span></div>
    <div class="fhead" style="left:244px;top:45px">Contact us</div>
    <div class="contact-row" style="top:65px"><svg viewBox="0 0 17 17"><circle cx="8.5" cy="8.5" r="8" fill="none" stroke="#fff"/><path d="M6 5.5l1.3-.3.8 1.8-.9.7a5 5 0 0 0 2.2 2.2l.7-.9 1.8.8-.3 1.3c-3 .3-5.8-2.6-5.6-5.6z" fill="#fff"/></svg>+ 555 (0142) 730</div>
    <div class="contact-row" style="top:97px"><svg viewBox="0 0 17 17"><circle cx="8.5" cy="8.5" r="8" fill="none" stroke="#fff"/><rect x="5" y="6" width="7" height="5" fill="none" stroke="#fff"/><path d="M5 6l3.5 3L12 6" fill="none" stroke="#fff"/></svg>contactus@novacoat.com</div>
    <div class="contact-row" style="top:129px"><svg viewBox="0 0 17 17"><circle cx="8.5" cy="8.5" r="8" fill="none" stroke="#fff"/><path d="M8.5 12.5s-3-3-3-5a3 3 0 0 1 6 0c0 2-3 5-3 5z" fill="none" stroke="#fff"/><circle cx="8.5" cy="7.5" r="1" fill="#fff"/></svg>Location: Elmridge, CT USA</div>
    <div class="fhead" style="left:417px;top:45px">Otherlinks</div>
    <ul class="links" style="left:417px"><li>Team</li><li>FAQ</li><li>Services</li><li>Privacy</li><li>Policy</li></ul>
    <div class="fhead" style="left:512px;top:45px">Quicklinks</div>
    <ul class="links" style="left:512px"><li>Home</li><li>About Us</li><li>where to buy</li><li>Products</li><li>More</li><li>Contact</li></ul>
    <div class="fhead" style="left:59px;top:205px">Sign up for newsletter</div>
    <div class="news"><div class="news__field"><svg viewBox="0 0 8 7"><rect x=".5" y=".5" width="7" height="6" fill="none" stroke="#f7c31a"/><path d="M.5 .5 4 4l3.5-3.5" fill="none" stroke="#f7c31a"/></svg>Enter Your Email:</div><div class="news__btn">Subscribe</div></div>
    <div class="badge" style="left:260px;width:60px"></div>
    <div class="badge" style="left:352px;width:128px"></div>
    <div class="badge" style="left:512px;width:60px"></div>
    <p class="abs center copyright">Copyright © 2022 Novacoat All right Reserved.</p>
  </footer>
</div>

</div>
</body>
</html>
```